businesscard, flyer and membercard

--------------------------------------------------------------------------------------------------
design flyer :
- delivering format (jpg, pdf and original psd)
- there is a example how the flyers should look like
the text and logo should be the same as the exemple flyer, the creativity is yours.
- the design should have a back and front side.
File format : 15,0 cm x 21,2 cm
design membercard :
- there is example how the member-card should look like
the text and logo should be the same as the exemple membercard, the creativity is yours.
- the front side contains text and open space where for writing :
Naam ......
Dansstijlen ......
- the front side contains 12 circels horizontal at the line name at the end of the line "Salsa".
- the front side contains 12 circels horizontal at the line name at the end of the line "Bachata".
- the front side contains 12 circels horizontal at the line name at the end of the line "Kizomba".
- each horizontal line with circels contains a different kind of color/design.
- file format: 7,6 cm x 10,7 cm
Business card :
- there is example how the businesscard should look like
the text and logo should be the same as the exemple buisinesscard, the creativity is yours.
- the design should have a back a front side
File format : 8,7 cm x 5,7 cm

Target Market(s)

Dancing :Salsa, Bachata and Kizomba

Colors

Designer to choose colors to be used in the design.

Requirements
Must have
• same text as seen on the examples.
Nice to have
• see the examples as attachments
Should not have
• - REMOVE TEXT "KOV" from the design
• - REMOVE TEXT "Gratis Parkeren"

```html
<!DOCTYPE html>
<html lang="nl">
<head>
<meta charset="utf-8">
<title>Gratis Proeflessen – Kestrel Dance Studio</title>
<link href="https://fonts.googleapis.com/css2?family=Open+Sans:ital,wght@0,400;0,600;0,800;1,400&family=Bowlby+One&display=swap" rel="stylesheet">
<style>
  :root {
    --bg: #dcdcdc;
    --charcoal: #2e2d2f;
    --crimson: #ad1f2a;
    --violet: #43235f;
    --amber: #f4a42a;
    --amber-deep: #ee8a1e;
    --white: #ffffff;
  }
  * { margin: 0; padding: 0; box-sizing: border-box; }
  html, body {
    width: 1200px; height: 900px; overflow: hidden;
    background: var(--bg);
  }
  .stage {
    width: 1200px; height: 900px;
    display: flex; align-items: center; justify-content: center;
  }
  .flyer {
    position: relative;
    width: 600px; height: 848px;
    background: var(--charcoal);
    overflow: hidden;
    font-family: "Open Sans", sans-serif;
    color: var(--white);
    box-shadow: 0 10px 30px rgba(0,0,0,.18);
  }
  .flyer-art { position: absolute; inset: 0; }
  .offer {
    position: absolute; left: 34px; top: 34px;
    font-weight: 800; text-transform: uppercase;
    font-size: 40px; line-height: 1.0; letter-spacing: .5px;
  }
  .offer-dates {
    display: block; font-size: 22px; margin-top: 6px; text-transform: none;
  }
  .studio-mark {
    position: absolute; right: 34px; top: 150px;
    display: flex; align-items: center; gap: 8px;
    font-weight: 800; font-size: 17px; letter-spacing: 1px; text-transform: uppercase;
    text-align: right; line-height: 1.2;
  }
  .studio-mark .dot {
    width: 12px; height: 12px; border-radius: 50%; background: var(--white);
  }
  .styles {
    position: absolute; left: 0; right: 0; top: 545px;
    font-family: "Bowlby One", sans-serif;
    font-size: 64px; line-height: .9; letter-spacing: 2px;
  }
  .styles span { display: block; }
  .styles .salsa { padding-left: 230px; }
  .styles .bachata { padding-left: 120px; }
  .styles .kizomba { padding-left: 220px; }
  .perks {
    position: absolute; left: 30px; top: 735px; width: 220px;
    text-align: right; font-size: 15px; line-height: 1.45;
  }
  .perks::before {
    content: ""; display: block; width: 34px; height: 3px;
    background: var(--white); margin: 0 0 8px auto;
  }
  .divider {
    position: absolute; left: 268px; top: 720px;
    width: 2px; height: 128px; background: var(--white);
  }
  .contact {
    position: absolute; left: 288px; top: 770px;
    font-size: 14px; line-height: 1.55;
  }
  .marker {
    position: absolute; width: 10px; height: 10px; border: 2px solid var(--white);
  }
</style>
</head>
<body>
<main class="stage">
  <article class="flyer">
    <svg class="flyer-art" viewBox="0 0 600 848" width="600" height="848">
      <defs>
        <radialGradient id="sun" cx="45%" cy="40%" r="65%">
          <stop offset="0" stop-color="#f8b23a"/>
          <stop offset="1" stop-color="var(--amber-deep)"/>
        </radialGradient>
        <linearGradient id="dancers" x1="0" y1="0" x2="0" y2="1">
          <stop offset="0" stop-color="#3a2a2a" stop-opacity=".9"/>
          <stop offset=".45" stop-color="#d9362f" stop-opacity=".85"/>
          <stop offset="1" stop-color="#1e1b1c" stop-opacity=".9"/>
        </linearGradient>
      </defs>
      <polygon class="field-red" points="0,0 70,0 470,330 150,848 0,690" fill="var(--crimson)"/>
      <polygon class="field-violet" points="600,300 600,848 300,848 470,330" fill="var(--violet)"/>
      <circle cx="290" cy="410" r="255" fill="none" stroke="#fff" stroke-width="1" opacity=".7"/>
      <circle cx="300" cy="400" r="205" fill="url(#sun)"/>
      <circle cx="300" cy="400" r="135" fill="none" stroke="#fff" stroke-width="1" opacity=".6"/>
      <line x1="0" y1="330" x2="600" y2="620" stroke="#fff" stroke-width="1" stroke-dasharray="3 4" opacity=".4"/>
      <circle cx="40" cy="400" r="5" fill="none" stroke="#fff" stroke-width="2"/>
      <circle cx="545" cy="480" r="5" fill="none" stroke="#fff" stroke-width="2"/>
      <rect x="170" y="180" width="330" height="620" rx="60" fill="url(#dancers)"
            role="img" aria-label="Foto van een dansend salsapaar: man in zwart, vrouw in rode jurk"/>
    </svg>

    <h1 class="offer">Gratis<br>Proeflessen<span class="offer-dates">26 T/M 28 Sept</span></h1>

    <div class="studio-mark"><span class="dot"></span><span>Kestrel<br>Dance Studio</span></div>
    <span class="marker" style="left:520px; top:248px;"></span>
    <span class="marker" style="left:515px; top:705px;"></span>

    <h2 class="styles">
      <span class="salsa">Salsa</span>
      <span class="bachata">Bachata</span>
      <span class="kizomba">Kizomba</span>
    </h2>

    <ul class="perks" style="list-style:none;">
      <li>Eerste les Gratis</li>
      <li>Studente Korting</li>
      <li>ELK niveau</li>
      <li>Alle leeftijden</li>
    </ul>

    <span class="divider"></span>

    <address class="contact" style="font-style:normal;">
      Lindelaan 14. 2514 KT Den Haag<br>
      Facebook: Kestreldenhaag<br>
      Tel: 06581729
    </address>
  </article>
</main>
</body>
</html>
```